Bright Meadow Counseling Business Card design with a visually interesting use of Space

I need business cards that are luxurious and give a peaceful, calm vibe. I also had some letterhead designed, and i like the look of it also, it's attached with the logo design for reference/ ideas but feel free to be creative.

Target Market(s)

High end luxurious client who needs counseling

Industry/Entity Type

Marriage and Family Therapy

Contact Information for Business Card

Mira Kowalczyk MS LMFT/ or Toby Hallett address 4150 Larkin Suite 600

Font styles to use
Sans Serif

Colors
0054AA
0677BA
7BADD7
CADEEF
E8F1F8
0094D4
00A9DD
6FCCEA
C7EBF8
E9F6FB
A7469A
B969AE
D3A5CF
EDDBEB
F8F0F9
6B429C
8869AF
B7A5CE
E3DAEB
F3F0F8

Requirements
Must have
• Logo and color scheme but be simple modern and luxurious
Nice to have
• I'd like to incorporate some elelmets from the logo and letterhead into a simple modern card

```html
<!DOCTYPE html>
<html lang="en">
<head>
<meta charset="utf-8">
<title>Bright Meadow Counseling — Business Card</title>
<link rel="stylesheet" href="https://fonts.googleapis.com/css2?family=Jost:wght@300&display=swap">
<style>
  :root {
    --page-bg: #f1f1f1;
    --card-bg: #ffffff;
    --ink: #1b1b1f;
    --brand-blue: #1276ba;
    --brand-navy: #16263c;
    --brand-magenta: #9b1f63;
    --brand-purple: #8869af;
    --ring-soft: #eeeeee;
  }
  html, body {
    margin: 0;
    width: 1200px;
    height: 1200px;
    overflow: hidden;
    background: var(--page-bg);
    font-family: "Jost", sans-serif;
    font-weight: 300;
  }
  .card {
    position: absolute;
    background: var(--card-bg);
    overflow: hidden;
  }
  .card--back  { left: 240px; top: 135px; width: 711px; height: 428px; }
  .card--front { left: 240px; top: 632px; width: 717px; height: 432px; }
  .card svg { display: block; }
  .name { fill: var(--ink); font-family: "Jost", sans-serif; font-weight: 300; }
  .contact-text { fill: var(--ink); font-size: 16px; font-family: "Jost", sans-serif; font-weight: 300; }
  .icon { fill: var(--brand-blue); }
  .icon-line { fill: none; stroke: var(--brand-blue); stroke-width: 1.3; }
</style>
</head>
<body>

<section class="card card--back" aria-label="Card back with contact details">
  <svg width="711" height="428" viewBox="0 0 711 428">
    <circle class="ring ring--blue" cx="698" cy="-1" r="109" fill="none" stroke="var(--brand-blue)" stroke-width="44"/>
    <circle class="ring ring--navy" cx="15" cy="440" r="134" fill="none" stroke="var(--brand-navy)" stroke-width="53"/>

    <g class="brand-name">
      <circle cx="262" cy="185" r="14" fill="var(--brand-purple)"/>
      <text class="name" x="248" y="240" font-size="30" text-anchor="end">Bright Meadow</text>
      <text class="name" x="248" y="262" font-size="17" text-anchor="end" letter-spacing="2.5">Counseling</text>
    </g>

    <rect class="divider" x="300" y="148" width="2.5" height="132" fill="var(--brand-blue)"/>

    <g class="contact-list">
      <!-- mobile -->
      <rect class="icon-line" x="323" y="150" width="9" height="15" rx="1.5"/>
      <circle class="icon" cx="327.5" cy="162" r="1"/>
      <text class="contact-text" x="345" y="163">369-480-1127</text>

      <!-- fax -->
      <rect class="icon-line" x="322" y="183" width="12" height="7" rx="1.5"/>
      <rect class="icon-line" x="325" y="179" width="6" height="4"/>
      <rect class="icon-line" x="325" y="187" width="6" height="4"/>
      <text class="contact-text" x="345" y="191">369-480-1190</text>

      <!-- email -->
      <rect class="icon" x="322" y="206" width="13" height="9"/>
      <path d="M322 206 L328.5 211.5 L335 206 M322 215 L327 210.5 M335 215 L330 210.5" fill="none" stroke="#fff" stroke-width="1"/>
      <text class="contact-text" x="344" y="216">info@brightmeadowcounsel.com</text>

      <!-- web -->
      <circle class="icon-line" cx="328.5" cy="237" r="6.5"/>
      <ellipse class="icon-line" cx="328.5" cy="237" rx="3" ry="6.5"/>
      <path class="icon-line" d="M322 237 H335 M323 233.5 H334 M323 240.5 H334"/>
      <text class="contact-text" x="345" y="242">www.brightmeadowcounsel.com</text>

      <!-- location -->
      <path class="icon" d="M328.5 258 a6 6 0 0 1 6 6 c0 4.5 -6 10 -6 10 s-6 -5.5 -6 -10 a6 6 0 0 1 6 -6z"/>
      <circle cx="328.5" cy="264" r="2.2" fill="#fff"/>
      <text class="contact-text" x="345" y="273">2218 Willow Bend Road Juneau, Alaska 99801</text>
    </g>
  </svg>
</section>

<section class="card card--front" aria-label="Card front with practice name">
  <svg width="717" height="432" viewBox="0 0 717 432">
    <circle class="ring ring--magenta" cx="18" cy="-11" r="135" fill="none" stroke="var(--brand-magenta)" stroke-width="56"/>
    <circle class="ring ring--soft" cx="60" cy="412" r="123" fill="none" stroke="var(--ring-soft)" stroke-width="48"/>
    <circle class="ring ring--navy" cx="710" cy="387" r="120" fill="none" stroke="var(--brand-navy)" stroke-width="48"/>

    <g class="brand-name">
      <circle cx="516" cy="158" r="40" fill="var(--brand-purple)"/>
      <text class="name" x="471" y="253" font-size="58" text-anchor="end">Bright Meadow</text>
      <text class="name" x="469" y="292" font-size="33" text-anchor="end" letter-spacing="5">Counseling</text>
    </g>
  </svg>
</section>

</body>
</html>
```